「ページリオ出版用(電子書籍)の本の表紙」デザインお願いします。

本のタイトル「古き言葉が明日を照らす鍵」

著者名「森川修平」

本のタイトルが他の本より目立つように
お願いします。(背景が宇宙空間で暗いので、白文字がより良いでしょうか?)

本表紙のイメージ「星々がきらめく(星には赤やピンク色の星が入って)宇宙空間に
「ミツルハカ(5首)の左巻螺旋図」が表紙の中央(表紙の3分の1を占める位の大きさで)に
配置され、その中央に「新潟県糸魚川産の緑色の勾玉(マガタマ)(マガタマの穴が右にあり、細い部分が左にある、ちょうどマガタマが横になった感じ)」が配置されてるイメージです。

(コンペ優勝者よりデザインをいただいた後、いただいたデザインに別の本のタイトルで(著者は一緒)お願いすることとなりますので宜しくお願い致します。)

タイトルの他にサブタイトルとして「大陸の起源は海辺?」「星々の3000音の母は岩絵の印!」を入れていただきたいです。

色、アピール度、当方の要望が全て満たされてるかで選びました。

今後あと10依頼させていただく予定ですので、今後ともよろしくお願いいたします。

```html
<!DOCTYPE html>
<html lang="ja">
<head>
<meta charset="utf-8">
<title>古き言葉が明日を照らす鍵</title>
<link href="https://fonts.googleapis.com/css2?family=M+PLUS+Rounded+1c:wght@500;800;900&display=swap" rel="stylesheet">
<style>
  :root {
    --space-deep: #070b1f;
    --space-navy: #10204a;
    --nebula-blue: #3f7fd0;
    --nebula-cyan: #7fc3e8;
    --nebula-amber: #a0602c;
    --nebula-rose: #b0487a;
    --planet-blue: #2a5fa8;
    --title-white: #ffffff;
    --title-ghost: rgba(190, 200, 230, 0.55);
    --text-shadow: rgba(0, 0, 20, 0.85);
  }
  html, body {
    margin: 0;
    padding: 0;
    width: 750px;
    height: 1200px;
    overflow: hidden;
    background: var(--space-deep);
  }
  .cover {
    position: relative;
    width: 750px;
    height: 1200px;
    overflow: hidden;
    font-family: "M PLUS Rounded 1c", sans-serif;
    color: var(--title-white);
  }
  .cover-art {
    position: absolute;
    inset: 0;
    background:
      radial-gradient(ellipse 260px 200px at 560px 520px, rgba(127,195,232,0.55), transparent 70%),
      radial-gradient(ellipse 380px 300px at 480px 420px, rgba(63,127,208,0.55), transparent 72%),
      radial-gradient(ellipse 300px 360px at 90px 760px, rgba(160,96,44,0.6), transparent 70%),
      radial-gradient(ellipse 200px 180px at 200px 300px, rgba(176,72,122,0.3), transparent 70%),
      radial-gradient(circle 520px at 780px 1180px, var(--planet-blue) 0%, rgba(42,95,168,0.6) 45%, transparent 72%),
      linear-gradient(180deg, var(--space-deep) 0%, var(--space-navy) 45%, #0b1436 80%, var(--space-deep) 100%);
  }
  .title-lead {
    position: absolute;
    left: 50px;
    margin: 0;
    font-weight: 800;
    line-height: 1;
    letter-spacing: 4px;
    text-shadow: 0 0 12px var(--text-shadow);
  }
  .title-lead--first { top: 22px; font-size: 92px; }
  .title-lead--second { top: 128px; font-size: 100px; }
  .title-key {
    position: absolute;
    top: 262px;
    left: 0;
    width: 750px;
    margin: 0;
    text-align: center;
    font-size: 290px;
    font-weight: 900;
    line-height: 1;
    letter-spacing: 10px;
    text-shadow:
      -14px -8px 0 var(--title-ghost),
      12px 10px 0 rgba(140,150,190,0.45),
      0 0 24px var(--text-shadow);
  }
  .title-tail {
    position: absolute;
    top: 620px;
    right: 20px;
    margin: 0;
    font-size: 80px;
    font-weight: 800;
    line-height: 1;
    letter-spacing: 2px;
    text-shadow: 0 0 12px var(--text-shadow);
  }
  .subtitles {
    position: absolute;
    top: 910px;
    left: 0;
    width: 750px;
    text-align: center;
    font-weight: 800;
    text-shadow: 0 0 10px var(--text-shadow), 2px 2px 0 var(--text-shadow);
  }
  .subtitle { margin: 0; line-height: 1.35; }
  .subtitle--first { font-size: 60px; }
  .subtitle--second { font-size: 47px; }
  .author {
    position: absolute;
    top: 1108px;
    left: 0;
    width: 750px;
    text-align: center;
    font-weight: 800;
    text-shadow: 0 0 8px var(--text-shadow);
  }
  .author-label { display: block; font-size: 18px; font-weight: 500; line-height: 1.2; }
  .author-name { display: block; font-size: 38px; line-height: 1.2; letter-spacing: 6px; }
</style>
</head>
<body>
  <main class="cover">
    <div class="cover-art" role="img" aria-label="星がきらめく宇宙空間と青い惑星、その上に散らばるミツルハカの円形図象と左巻螺旋図"></div>

    <h1 class="title">
      <span class="title-lead title-lead--first">古き言葉が</span>
      <span class="title-key">明日</span>
      <span class="title-tail">を照らす鍵</span>
    </h1>

    <div class="subtitles">
      <p class="subtitle subtitle--first">大陸の起源は海辺?</p>
      <p class="subtitle subtitle--second">星々の3000音の母は岩絵の印!</p>
    </div>

    <p class="author">
      <span class="author-label">著者</span>
      <span class="author-name">森川 修平</span>
    </p>
  </main>
</body>
</html>
```